Dental Health Door hanger for contest to attract new patients

We are a group dental practice located in Burlington, Ontario, Canada. We are looking to bring in new patients and are targeting a new subdivision as well as established neighbourhoods around it.

The door hanger we require is for a contest are offering that will run for approx. 6 months to win a $1000.00 travel gift card. The individual must come in person to drop off the ballot and during that time they will get a tour of the practice and meet key people. There is no requirement for them to make an appointment but that is the ultimate goal.

I have included:
- a picture we typically use, however it is not required (female smiling)
- Our logo with "your city your dentists" below it. We want that tagline removed
- our other logo
- the excel version of the map created to our location
- the current one attempted on our own and is missing something - like the concept but not the total look/ feel

The final design should make the person want to come in and book an appointment with us and at the very least call to schedule something with a dentist.

Target Market(s)

New subdivision and surrounding area for new patients

Industry/Entity Type

Dental Clinic

Colors

Designer to choose colors to be used in the design.

Requirements
Must have
• Our address is 1846 Pemberly Road, Burlington, Ontario L7M 2K8. Our phone number is 905-482-7150. We are located on the 3rd floor of the Corvane Family Health Centre.
Nice to have
• We only need to have a logo, our address, a ballot of some sort on the door hanger and the details about the contest, the rest is up to you. We are moving towards the slogan "what makes you smile" at some point so this can be incorporated if it works with the overall design.
Should not have
• Fluorescent colours

```html
<!DOCTYPE html>
<html lang="en">
<head>
<meta charset="utf-8">
<title>Brightway Dental Group – Contest Door Hanger</title>
<link rel="stylesheet" href="https://fonts.googleapis.com/css2?family=Marcellus+SC&family=Libre+Baskerville:ital,wght@0,400;0,700;1,400&family=Open+Sans:wght@400;600&display=swap">
<style>
  :root {
    --backdrop: #232323;
    --brand-blue: #356db8;
    --gold: #e7b94a;
    --gold-deep: #d7a73a;
    --ink: #111111;
    --paper: #ffffff;
    --form-bg: #f3f3f3;
    --tagline: #e8b73c;
  }
  * { box-sizing: border-box; margin: 0; padding: 0; }
  html, body { width: 1200px; height: 1200px; overflow: hidden; background: var(--backdrop); }
  .hanger {
    position: absolute; left: 190px; top: 70px; width: 820px; height: 1060px;
    background: var(--paper); overflow: hidden;
  }
  .top-band { position: absolute; left: 0; top: 0; width: 100%; height: 50px; background: var(--brand-blue); }
  .header {
    position: absolute; left: 40px; top: 30px; width: 740px; height: 140px;
    background: var(--paper); border-radius: 14px 14px 0 0;
  }
  .brand-name {
    position: absolute; left: 30px; bottom: 22px;
    font-family: "Marcellus SC", serif; font-size: 46px; color: var(--ink); letter-spacing: 1px;
  }
  .brand-mark {
    position: absolute; right: 40px; top: 24px; width: 86px; height: 86px; background: var(--brand-blue);
  }
  .hero {
    position: absolute; left: 0; top: 170px; width: 100%; height: 390px;
    background: linear-gradient(120deg, #b8b2ad 0%, #6b5348 35%, #3b2b25 60%, #c9c3c0 100%);
  }
  .contact {
    position: absolute; right: 40px; top: 250px; color: var(--paper);
    font-family: "Libre Baskerville", serif; font-size: 16px; text-align: right; line-height: 1.9;
  }
  .contact svg { width: 18px; height: 18px; vertical-align: -3px; margin-left: 6px; }
  .tagline-strip {
    position: absolute; left: 0; top: 500px; width: 460px; height: 60px; background: var(--ink);
  }
  .tagline {
    position: absolute; left: 24px; top: 509px;
    font-family: "Libre Baskerville", serif; font-weight: 700; font-size: 33px; color: var(--tagline);
    white-space: nowrap;
  }
  .visit-panel { position: absolute; left: 0; top: 560px; width: 460px; height: 500px; background: var(--gold); }
  .visit-heading { position: absolute; left: 40px; top: 18px; font-family: "Libre Baskerville", serif; color: var(--ink); }
  .visit-heading .stop { font-size: 28px; font-weight: 700; display: block; }
  .visit-heading .meet { font-size: 20px; display: block; margin-top: 2px; }
  .visit-heading .win { font-size: 38px; font-weight: 700; display: block; margin-left: 150px; margin-top: -6px; }
  .location-map {
    position: absolute; left: 40px; top: 140px; width: 380px; height: 200px;
    background: var(--gold-deep); border-radius: 4px;
  }
  .visit-details {
    position: absolute; left: 40px; top: 360px; width: 390px;
    font-family: "Libre Baskerville", serif; font-size: 15.5px; line-height: 1.55; color: var(--ink);
  }
  .visit-details svg { width: 28px; height: 30px; display: block; margin-bottom: 6px; }
  .ballot {
    position: absolute; left: 460px; top: 500px; width: 360px; height: 260px; background: var(--form-bg);
    padding: 24px 30px 0 30px; font-family: "Open Sans", sans-serif; font-size: 13px; color: var(--ink);
  }
  .ballot .cut-line { border-top: 2px dashed var(--ink); margin-bottom: 14px; }
  .ballot .field { border-bottom: 1.5px solid var(--ink); height: 34px; display: flex; align-items: flex-end; padding-bottom: 3px; gap: 120px; }
  .prize-panel {
    position: absolute; left: 460px; top: 760px; width: 360px; height: 300px; background: var(--brand-blue);
    color: var(--paper); font-family: "Libre Baskerville", serif; text-align: center; padding-top: 40px;
  }
  .prize-panel .lead { font-size: 24px; letter-spacing: 1px; }
  .prize-panel .amount { font-size: 82px; font-weight: 700; line-height: 1.1; }
  .prize-panel .item { font-size: 24px; letter-spacing: 1px; }
  .deadline {
    position: absolute; left: 400px; top: 1000px; width: 360px; height: 60px; background: var(--ink);
    border-radius: 14px 14px 0 0; color: var(--tagline);
    font-family: "Libre Baskerville", serif; font-style: italic; font-size: 22px;
    display: flex; align-items: center; justify-content: center;
  }
</style>
</head>
<body>
  <main class="hanger">
    <div class="top-band"></div>
    <header class="header">
      <div class="brand-name">Brightway Dental Group</div>
      <div class="brand-mark"></div>
    </header>

    <div class="hero" role="img" aria-label="Photo of a smiling woman in a knit winter hat outdoors"></div>

    <div class="contact">
      <div>www.brightwaydental.ca
        <svg viewBox="0 0 20 20" fill="none" stroke="#fff" stroke-width="1.5"><circle cx="10" cy="10" r="8"/><ellipse cx="10" cy="10" rx="3.5" ry="8"/><line x1="2" y1="10" x2="18" y2="10"/></svg>
      </div>
      <div>Phone: 905-482-7150
        <svg viewBox="0 0 20 20"><circle cx="10" cy="10" r="9" fill="#fff"/><path d="M6.5 5.5l2 0 1 2.5-1.3 1a6 6 0 0 0 2.8 2.8l1-1.3 2.5 1v2c-4.5.5-8.5-3.5-8-8z" fill="#232323"/></svg>
      </div>
    </div>

    <div class="tagline-strip"></div>
    <div class="tagline">Your City Your Dentists</div>

    <section class="visit-panel">
      <h2 class="visit-heading">
        <span class="stop">Stop By</span>
        <span class="meet">Meet The Team Enter</span>
        <span class="win">To Win!</span>
      </h2>
      <div class="location-map" role="img" aria-label="Street map showing the clinic location"></div>
      <div class="visit-details">
        <svg viewBox="0 0 28 30" fill="none" stroke="#111" stroke-width="2"><path d="M10 20s-7-7-7-11a7 7 0 0 1 14 0c0 4-7 11-7 11z" fill="#111"/><circle cx="10" cy="9" r="2.5" fill="#e7b94a" stroke="none"/><path d="M4 22l-2 6h24l-4-6h-6"/></svg>
        Come in person to submit your ballot at our Address : 1846 Pemberly Road, Burlington, Ontario L7M 2K8. We are located on the 3rd floor of the Corvane Family Health Centre.
      </div>
    </section>

    <section class="ballot">
      <div class="cut-line"></div>
      <div class="field">Name</div>
      <div class="field"><span>Address</span><span>Postal Code</span></div>
      <div class="field">City</div>
      <div class="field">Phone</div>
      <div class="field">Email Address</div>
    </section>

    <section class="prize-panel">
      <div class="lead">ENTER TO WIN A</div>
      <div class="amount">$1000</div>
      <div class="item">TRAVEL GIFT CARD</div>
    </section>

    <div class="deadline">Contest closes July 15, 2019</div>
  </main>
</body>
</html>
```